Dane Morrow films- wedding and event films company website. DESKTOP AND MOBILE

We need a website for a high-end wedding and event film production company. Looking for a very modern and elegant design. my old website is www.danemorrowfilms.example

I like the "white/black/rose gold" color scheme of my logo.

really looking for a sleek modern design the breaths professional and artistic.

Target Market(s)

wedding and event films.

Industry/Entity Type

Film Production

Number of Pages Required

5+ page

Colors

Designer to choose colors to be used in the design.

Requirements
Must have
• website name will be www.danemorrowfilms.example
• tagline is "CINEMATIC STORIES ABOUT YOU"
• sections: HOME, CONTACT, ABOUT, FILMS, BLOG
• You can see my old website at danemorrowfilms.example
• Website about section:
• Dane Morrow Films was Established with the basis of truly cinematic and artistic films in mind. Dane and his team routinely travel the globe documenting weddings and events for high profile clients and discerning couples. Dane was born and raised in Maui Hawaii and has a unique approach to his films that embody the essence of a Hollywood film. Dane has spent the last 10 years traveling the world documenting corporate events and weddings with multiple Award winning production companies. In 2017 Dane decided to establish his own brand “Dane Morrow films” that will take everything he has learned with his past experiences and push it to the next level. Aside from his personal achievements, Dane is extremely passionate about his craft and always looks forward to handcrafting beautiful wedding/event films for his clients. The style of work is non-traditional and the day of filming is extremely unobtrusive (as we are looking for natural-candid/ raw emotions).
• If you are looking for the best price in town, we are probably not the best option, but if you’re looking for the best quality and peace of mind on your wedding day, then you’re in the right place. Dane Morrow Films is a boutique studio that only accepts a limited number of assignments per year. Inquire early to ensure availability.
• LINKS TO VIMEO VIDEOS THAT WILL BE IN THE "FILMS' SECTION.
• BRENT FILM TRAILER - https://clipvault.example/508114362
• BRENT FEATURE FILM - https://clipvault.example/617392048
• JUNE AND ROB'S WEDDING - https://clipvault.example/724958160
• DRONE DEMO REEL - https://clipvault.example/841576203
• WEDDING INDUSTRY EVENT PARTY - https://clipvault.example/962304817/a8d3e7b21c
• images that you can use on site are here: https://brigittolsenimages.proofbox.example/gallery/nora&felix/
• password is: meadow

```html
<!DOCTYPE html>
<html lang="en">
<head>
<meta charset="utf-8">
<title>Dane Morrow Films — Cinematic Stories About You</title>
<link href="https://fonts.googleapis.com/css2?family=Old+Standard+TT:wght@400&family=Montserrat:wght@400;500;600&display=swap" rel="stylesheet">
<style>
  :root{
    --black:#000;
    --white:#fff;
    --rose:#a86d4b;
    --rose-text:#a5684a;
    --ink:#1d1d1d;
    --muted:#8a8a8a;
    --panel:#f2f2f2;
    --serif:'Old Standard TT', Georgia, serif;
    --sans:'Montserrat', Helvetica, Arial, sans-serif;
  }
  *{box-sizing:border-box;margin:0;padding:0}
  html,body{width:891px;height:1200px;overflow:hidden;background:var(--white)}
  .page{position:relative;width:891px;height:1200px;font-family:var(--serif);color:var(--ink)}

  .site-header{position:absolute;left:0;top:0;width:891px;height:67px;background:var(--black)}
  .brand{position:absolute;left:0;width:891px;top:30px;text-align:center}
  .brand-name{font-family:var(--sans);font-weight:500;font-size:9px;letter-spacing:1.2px;color:var(--white)}
  .brand-tagline{margin-top:9px;font-family:var(--sans);font-size:4.5px;letter-spacing:1.2px;color:var(--rose)}
  .menu-toggle{position:absolute;left:793px;top:30px}

  .hero{position:absolute;left:0;top:67px;width:891px;height:354px;
    background:linear-gradient(165deg,#e8d8c4 0%,#c9b7a2 28%,#8c8479 48%,#6f6a62 70%,#3d3a35 100%)}
  .hero-card{position:absolute;left:565px;top:284px;width:243px;height:179px;background:var(--rose);color:var(--white);padding:25px 22px}
  .hero-card .lead{font-size:12.5px;line-height:15.5px}
  .hero-card .statement{margin-top:14px;font-size:20px;line-height:26px}
  .read-more{position:absolute;left:22px;top:191px;top:auto;bottom:23px;display:flex;align-items:center;gap:9px;font-family:var(--sans);font-weight:600;font-size:4.5px;letter-spacing:1px}

  .slider-nav{position:absolute;left:84px;top:441px;display:flex;gap:13px;font-size:7px;color:var(--ink)}
  .slider-nav span{display:flex;align-items:center;gap:5px}

  .testimonial{position:absolute;left:0;top:463px;width:891px;height:326px}
  .side-label{position:absolute;left:76px;top:689px;transform:rotate(-90deg);transform-origin:left top;font-family:var(--sans);font-size:4.5px;letter-spacing:1px;color:var(--muted);white-space:nowrap}
  .side-rule{position:absolute;left:81px;top:564px;width:1px;height:31px;background:#c9c9c9}
  .quote{position:absolute;left:0;top:577px;width:891px;text-align:center;font-size:24px;line-height:28px;color:var(--ink)}
  .quote-author{position:absolute;left:0;top:659px;width:891px;text-align:center;font-family:var(--sans);font-size:5px;letter-spacing:1px;color:var(--rose-text)}

  .featured{position:absolute;left:0;top:789px;width:891px;height:333px;background:var(--panel)}
  .section-label{position:absolute;left:0;top:41px;width:891px;text-align:center;font-family:var(--sans);font-weight:600;font-size:4.8px;letter-spacing:1px}
  .article{position:absolute;top:79px;width:228px}
  .article-image{width:228px;height:116px;background:linear-gradient(180deg,#dfe6ea 0%,#b9c3bf 45%,#5e6d55 70%,#ede9e2 100%)}
  .article-title{margin-top:9px;font-size:14.5px;line-height:17px;color:var(--rose-text)}
  .article-date{margin-top:6px;font-family:var(--sans);font-weight:500;font-size:4.5px;letter-spacing:.4px}
  .article-excerpt{margin-top:10px;font-size:7.5px;line-height:9.3px;color:#333}

  .site-footer{position:absolute;left:0;top:1122px;width:891px;height:78px}
  .footer-nav{position:absolute;left:83px;top:33px;display:flex;gap:13px;font-family:var(--sans);font-weight:500;font-size:5px;letter-spacing:1px}
  .copyright{position:absolute;left:83px;top:44px;font-family:var(--sans);font-weight:500;font-size:5px;letter-spacing:1px}
  .contact-box{position:absolute;top:28px;height:25px;border:1px solid var(--rose);color:var(--rose-text);font-size:7px;display:flex;align-items:center;justify-content:center}
  .contact-email{left:590px;width:125px}
  .contact-phone{left:733px;width:73px}
</style>
</head>
<body>
<div class="page">

  <header class="site-header">
    <div class="brand">
      <div class="brand-name">DANE MORROW FILMS</div>
      <div class="brand-tagline">CINEMATIC STORIES ABOUT YOU</div>
    </div>
    <svg class="menu-toggle" width="14" height="6" viewBox="0 0 14 6" aria-label="Menu">
      <rect y="0" width="14" height="1" fill="#a86d4b"/>
      <rect y="2.5" width="14" height="1" fill="#a86d4b"/>
      <rect y="5" width="14" height="1" fill="#a86d4b"/>
    </svg>
  </header>

  <div class="hero" role="img" aria-label="Bride and groom embracing on a rocky seaside path at sunset"></div>

  <aside class="hero-card">
    <p class="lead">Are looking for the<br>best quality &amp; peace of mind<br>on your wedding day?</p>
    <p class="statement">Then you’re in the<br>right place.</p>
    <div class="read-more">READ MORE
      <svg width="22" height="3" viewBox="0 0 22 3"><line x1="0" y1="1.5" x2="22" y2="1.5" stroke="#fff" stroke-width=".6"/><circle cx="1" cy="1.5" r="1" fill="#fff"/></svg>
    </div>
  </aside>

  <nav class="slider-nav">
    <span><svg width="10" height="4" viewBox="0 0 10 4"><path d="M10 2H1M2.5 .5L1 2l1.5 1.5" stroke="#1d1d1d" fill="none" stroke-width=".8"/></svg>Prev</span>
    <span>Next<svg width="10" height="4" viewBox="0 0 10 4"><path d="M0 2h9M7.5 .5L9 2 7.5 3.5" stroke="#1d1d1d" fill="none" stroke-width=".8"/></svg></span>
  </nav>

  <section class="testimonial-block">
    <div class="side-rule"></div>
    <div class="side-label">WHAT PEOPLE SAY ABOUT US?</div>
    <blockquote class="quote">“Dane really is one of the best film makers in Hawaii,<br>great work Dane! We loved the film!”</blockquote>
    <div class="quote-author">— MARA LINDQVIST</div>
  </section>

  <section class="featured">
    <div class="section-label">FEATURED ARTICLE</div>
    <article class="article" style="left:90px">
      <div class="article-image" role="img" aria-label="Outdoor wedding ceremony with officiant, bride and groom among white flowers"></div>
      <h3 class="article-title">Lorem ipsum dolor sit amet,<br>consectetur adipiscing elit.</h3>
      <div class="article-date">31/10/2017</div>
      <p class="article-excerpt">Donec sollicitudin felis in orci ullamcorper, at vulputate ligula fermentum. Sed at lacus eget dolor rutrum inter dum ac quis nibh.</p>
    </article>
    <article class="article" style="left:332px">
      <div class="article-image" role="img" aria-label="Outdoor wedding ceremony with officiant, bride and groom among white flowers"></div>
      <h3 class="article-title">Lorem ipsum dolor sit amet,<br>consectetur adipiscing elit.</h3>
      <div class="article-date">31/10/2017</div>
      <p class="article-excerpt">Donec sollicitudin felis in orci ullamcorper, at vulputate ligula fermentum. Sed at lacus eget dolor rutrum inter dum ac quis nibh.</p>
    </article>
    <article class="article" style="left:573px">
      <div class="article-image" role="img" aria-label="Outdoor wedding ceremony with officiant, bride and groom among white flowers"></div>
      <h3 class="article-title">Lorem ipsum dolor sit amet,<br>consectetur adipiscing elit.</h3>
      <div class="article-date">31/10/2017</div>
      <p class="article-excerpt">Donec sollicitudin felis in orci ullamcorper, at vulputate ligula fermentum. Sed at lacus eget dolor rutrum inter dum ac quis nibh.</p>
    </article>
  </section>

  <footer class="site-footer">
    <nav class="footer-nav"><span>HOME</span><span>ABOUT</span><span>FILMS</span><span>BLOG</span><span>CONTACT</span></nav>
    <div class="copyright">© 2017 DANE MORROW FILMS</div>
    <div class="contact-box contact-email">dane@danemorrowfilms.example</div>
    <div class="contact-box contact-phone">(808) 555-0143</div>
  </footer>

</div>
</body>
</html>
```